FotoVELTA buisnesscard

Hey :) I need a modern buisnesscard for my company FotoVELTA
It most have:
Dagligleder og Fotograf: Henrik Torvald Bjelland

Mob: +4791642058
Epost: post@fotovelta.no
Adresse: Bakkestien22, 5412 Fjellvik

Facbook and instagram logo with text FotoVELTA

FotoVELTA logo

It Company

```html
<!DOCTYPE html>
<html lang="no">
<head>
<meta charset="utf-8">
<title>FotoVELTA – visittkort</title>
<link href="https://fonts.googleapis.com/css2?family=Montserrat:wght@500;700&family=Open+Sans:wght@400;600&display=swap" rel="stylesheet">
<style>
  :root {
    --backdrop: #2e2e30;
    --card-white: #ffffff;
    --brand-pink: #e083b6;
    --brand-blue: #2b8cc4;
    --ink: #1a1a1a;
  }
  * { box-sizing: border-box; margin: 0; padding: 0; }
  html, body {
    width: 1200px; height: 997px; overflow: hidden;
    background: var(--backdrop);
  }
  .canvas { position: relative; width: 1200px; height: 997px; }
  .card {
    position: absolute; width: 560px; height: 320px;
    border-radius: 3px;
    box-shadow: 0 12px 30px rgba(0,0,0,.45);
  }
  .card--front { left: 60px; top: 150px; background: var(--card-white); }
  .card--back { left: 580px; top: 527px; background: var(--brand-pink); }

  .brand {
    position: absolute; left: 40px; top: 128px;
    display: flex; align-items: center; gap: 12px;
  }
  .brand__mark { width: 30px; height: 30px; background: var(--brand-pink); }
  .brand__name {
    font-family: 'Montserrat', sans-serif; font-weight: 700;
    font-size: 40px; color: var(--brand-blue); letter-spacing: .5px;
  }

  .person { position: absolute; left: 300px; top: 34px; }
  .person__name {
    font-family: 'Montserrat', sans-serif; font-weight: 700;
    font-size: 19px; color: var(--brand-pink);
  }
  .person__role {
    font-family: 'Open Sans', sans-serif; font-size: 15px;
    color: var(--ink); margin-top: 2px;
  }

  .contact, .address {
    position: absolute; left: 330px;
    font-family: 'Open Sans', sans-serif; font-size: 15px;
    color: var(--ink); line-height: 1.45;
  }
  .contact { top: 120px; }
  .address { top: 214px; left: 360px; }

  .social {
    position: absolute; left: 40px; bottom: 30px;
    list-style: none;
    font-family: 'Open Sans', sans-serif; font-size: 16px; color: var(--ink);
  }
  .social__item { display: flex; align-items: center; gap: 10px; margin-top: 8px; }
  .social__item:nth-child(2) { margin-left: 18px; }
  .social__icon { width: 22px; height: 22px; background: var(--ink); border-radius: 4px; }

  .back-name {
    position: absolute; inset: 0;
    display: flex; align-items: center; justify-content: center;
    font-family: 'Montserrat', sans-serif; font-weight: 700;
    font-size: 44px; color: var(--card-white); letter-spacing: 1px;
  }
</style>
</head>
<body>
<main class="canvas">
  <section class="card card--front" aria-label="Visittkort forside">
    <div class="brand">
      <span class="brand__mark"></span>
      <span class="brand__name">FotoVELTA</span>
    </div>
    <div class="person">
      <p class="person__name">Henrik Torvald Bjelland</p>
      <p class="person__role">Dagligleder og Fotograf</p>
    </div>
    <div class="contact">
      <p>+4791642058</p>
      <p>post@fotovelta.no</p>
    </div>
    <div class="address">
      <p>Bakkestien22</p>
      <p>5412 Fjellvik, Norway</p>
    </div>
    <ul class="social">
      <li class="social__item"><span class="social__icon"></span>FotoVELTA</li>
      <li class="social__item"><span class="social__icon"></span>FotoVELTA</li>
    </ul>
  </section>

  <section class="card card--back" aria-label="Visittkort bakside">
    <p class="back-name">FotoVELTA</p>
  </section>
</main>
</body>
</html>
```